Thornwell Building Company - advertisement poster

I am looking to print some canvas signs to advertise my general contracting company, Thornwell Building Company. The sign will measure 6' long x 3' high so the size should match that ratio. I already have a logo icon, which is the Letter 'A' and some trees that I would like to incorporate, see attached. I would also like the to have the following information listed:
1) phone number: 472-318-6095
2) email: thornwellbuildingcompany@mailvistra.net
3) website: thornwellbuildingcompany.com
4) Lic#5386204
5) I want to use this text: "BUILD WITH THE T-CREW!"

The ad should be relatively simple and clean. Black and Green are my company colors. I am open to creative ideas!

Target Market(s)

People looking to renovate their homes

Industry/Entity Type

Construction

Colors
59FF00
82FF00
B8FF75
E3FFCB
F4FFEA

Requirements
Must have
• Must have my company logo
Should not have
• No photos or complex graphics

```html
<!DOCTYPE html>
<html lang="en">
<head>
<meta charset="utf-8">
<title>Thornwell Building Company – Sign</title>
<link rel="stylesheet" href="https://fonts.googleapis.com/css2?family=Michroma&family=Montserrat:wght@800;900&family=Poppins:wght@400;500&display=swap">
<style>
  :root {
    --backdrop: #7f7b7c;
    --sign-black: #000000;
    --brand-green: #6ab334;
    --ink-white: #ffffff;
  }
  * { margin: 0; padding: 0; box-sizing: border-box; }
  html, body {
    width: 1200px;
    height: 730px;
    overflow: hidden;
    background: var(--backdrop);
  }
  .sign {
    position: absolute;
    left: 0;
    top: 65px;
    width: 1200px;
    height: 600px;
    background: var(--sign-black);
    overflow: hidden;
  }
  .sign-art {
    position: absolute;
    inset: 0;
    width: 1200px;
    height: 600px;
  }
  .headline { font-family: "Montserrat", sans-serif; font-weight: 900; }
  .headline-green { fill: var(--brand-green); }
  .headline-white { fill: var(--ink-white); }
  .tech { font-family: "Michroma", sans-serif; }
  .phone-number { fill: var(--ink-white); }
  .license-label, .license-number { fill: var(--ink-white); }
  .brand-name { fill: var(--ink-white); }

  .contact-list {
    position: absolute;
    left: 62px;
    top: 398px;
    list-style: none;
    font-family: "Poppins", sans-serif;
    font-weight: 400;
    font-size: 23px;
    color: var(--ink-white);
  }
  .contact-item {
    display: flex;
    align-items: center;
    height: 30px;
    margin-bottom: 17px;
    white-space: nowrap;
  }
  .contact-icon {
    width: 28px;
    height: 28px;
    margin-right: 22px;
    flex: none;
  }
  .web-name { color: var(--brand-green); font-weight: 500; }
</style>
</head>
<body>
<main class="sign">
  <svg class="sign-art" viewBox="0 0 1200 600" xmlns="http://www.w3.org/2000/svg">
    <!-- right accent wedge -->
    <polygon class="accent-wedge" points="1141,0 1200,0 1200,459 1014,214" fill="var(--brand-green)"/>

    <!-- headline -->
    <text class="headline headline-green" x="57" y="154" font-size="120" textLength="909" lengthAdjust="spacingAndGlyphs">BUILD WITH</text>
    <text class="headline headline-green" transform="translate(88 277) rotate(-90)" font-size="40" textLength="107" lengthAdjust="spacingAndGlyphs">THE</text>
    <text class="headline headline-white" x="105" y="273" font-size="140" textLength="677" lengthAdjust="spacingAndGlyphs">T-CREW!</text>

    <!-- phone band -->
    <polygon class="phone-band" points="0,299 826,299 790,374 0,374" fill="var(--brand-green)"/>
    <circle cx="80" cy="337" r="21" fill="var(--sign-black)"/>
    <path d="M72 327c1.5-1.5 3.2-1 4 .5l2 3.5c.7 1.2.3 2.4-.8 3.2l-1.3 1c1 2.6 3.2 4.8 5.8 5.8l1-1.3c.8-1.1 2-1.5 3.2-.8l3.5 2c1.5.8 2 2.5.5 4-2 2-4.5 2.8-7.5 1.5-5.2-2.3-9.3-6.4-11.6-11.6-1.3-3-.5-5.8 1.2-7.8z" fill="var(--brand-green)"/>
    <text class="tech phone-number" x="117" y="362" font-size="64" textLength="615" lengthAdjust="spacingAndGlyphs">472-318-6095</text>

    <!-- license -->
    <rect x="66.5" y="500.5" width="318" height="45" fill="none" stroke="var(--brand-green)" stroke-width="3"/>
    <rect x="383" y="499" width="279" height="48" fill="var(--brand-green)"/>
    <text class="tech license-label" x="94" y="532" font-size="24" textLength="256" lengthAdjust="spacingAndGlyphs">LICENSE NO.</text>
    <text class="tech license-number" x="408" y="532" font-size="24" textLength="214" lengthAdjust="spacingAndGlyphs">#5386204</text>

    <!-- company name -->
    <circle class="brand-dot" cx="934" cy="370" r="62" fill="var(--brand-green)"/>
    <text class="tech brand-name" x="934" y="510" font-size="50" text-anchor="middle" textLength="456" lengthAdjust="spacingAndGlyphs">THORNWELL</text>
    <text class="tech brand-name" x="934" y="547" font-size="22" text-anchor="middle" textLength="456" lengthAdjust="spacingAndGlyphs">BUILDING COMPANY</text>
  </svg>

  <ul class="contact-list">
    <li class="contact-item">
      <svg class="contact-icon" viewBox="0 0 28 28" aria-hidden="true">
        <circle cx="14" cy="14" r="13" fill="var(--brand-green)"/>
        <rect x="7" y="9" width="14" height="10" fill="none" stroke="var(--sign-black)" stroke-width="1.6"/>
        <path d="M7 9l7 6 7-6" fill="none" stroke="var(--sign-black)" stroke-width="1.6"/>
      </svg>
      <span class="contact-email">thornwellbuildingcompany@mailvistra.net</span>
    </li>
    <li class="contact-item">
      <svg class="contact-icon" viewBox="0 0 28 28" aria-hidden="true">
        <circle cx="14" cy="14" r="13" fill="var(--brand-green)"/>
        <g fill="none" stroke="var(--sign-black)" stroke-width="1.4">
          <circle cx="14" cy="14" r="7.5"/>
          <ellipse cx="14" cy="14" rx="3.2" ry="7.5"/>
          <path d="M6.5 14h15M8 10h12M8 18h12"/>
        </g>
      </svg>
      <span class="contact-web">www.<span class="web-name">thornwellbuildingcompany</span>.com</span>
    </li>
  </ul>
</main>
</body>
</html>
```